Locksmith Business Cards

My father-in-law is in need of new business cards for his locksmith business and I need to impress him. Kindly help me out!

You can see the previous business card attached. It is a family run business in North Wales.

No individual names on the cards.

Key Things to Feature:
- The words "Prompt", "Local", "Reliable" (as you can see under the logo on the website)
- 24h Emergency Service
- Covering All of North Wales, the Wirral and Chester
- The color blue
- A key or a lock would be interesting (similar to the ones that come up when you google locksmith business card)

Optional (only if design includes bullet points, like the example below):
https://imgvaultcdnx.net/design_img/318264/57190/57190_2749031_318264_image.jpg
- Residential / Commercial / Automotive
- Alarms & Cameras
- Key Cutting & Safes

https://www.bryncoed-locksmiths-demo.co.uk/

Locksmith

01632 960 418
07700 900 362
bryncoedlocksmiths@mailvalex.com
Bryncoed Locksmiths, Hafod Barn, 4 Pennant Rd., Llandudno LL39 7QZ
www.bryncoed-locksmiths-demo.co.uk

• - The words "Prompt", "Local", "Reliable" (as you can see under the logo on the website)
• - 24h Emergency Service
• - Covering All of North Wales, the Wirral and Chester
• - A key or a lock would be interesting (similar to the ones that come up when you google locksmith business card)

```html
<!DOCTYPE html>
<html lang="en">
<head>
<meta charset="utf-8">
<title>Bryncoed Locksmiths – Business Card</title>
<link href="https://fonts.googleapis.com/css2?family=Lato:wght@400;700;900&display=swap" rel="stylesheet">
<style>
  :root {
    --ink: #1d1d1d;
    --card-dark: #1f1f1f;
    --paper: #ffffff;
    --brand-blue: #26a9e0;
    --text-light: #ffffff;
    --text-dark: #222222;
    --stage: #2a2a2a;
  }
  * { box-sizing: border-box; margin: 0; padding: 0; }
  html, body {
    width: 1200px; height: 895px; overflow: hidden;
    background: var(--stage);
    font-family: "Lato", Arial, sans-serif;
  }
  .stage {
    width: 1200px; height: 895px;
    display: flex; flex-direction: column; align-items: center; justify-content: center;
    gap: 28px;
  }
  .card {
    position: relative;
    width: 720px; height: 411px;
    overflow: hidden;
    box-shadow: 0 10px 30px rgba(0,0,0,.45);
  }

  /* Front */
  .card--front { background: var(--card-dark); color: var(--text-light); }
  .brand {
    position: absolute; left: 60px; top: 56px;
    display: flex; align-items: center; gap: 18px;
  }
  .brand__dot {
    width: 58px; height: 58px; border-radius: 50%;
    background: var(--brand-blue);
  }
  .brand__name {
    font-weight: 900; font-size: 44px; letter-spacing: .5px;
    color: var(--text-light);
  }
  .brand--on-paper .brand__name { color: var(--ink); font-size: 36px; }
  .brand--on-paper .brand__dot { width: 48px; height: 48px; background: var(--ink); }

  .services {
    position: absolute; left: 60px; right: 60px; top: 160px;
    display: flex; justify-content: space-between;
    list-style: none; font-size: 17px; letter-spacing: .6px;
  }
  .services li { display: flex; align-items: center; gap: 10px; }
  .services li::before {
    content: ""; width: 12px; height: 12px; border-radius: 50%;
    background: var(--brand-blue);
  }
  .values {
    position: absolute; left: 0; right: 0; top: 222px;
    text-align: center; font-size: 18px; letter-spacing: 2px; font-weight: 700;
  }
  .values .sep { margin: 0 14px; font-weight: 400; }
  .coverage {
    position: absolute; left: 0; right: 0; top: 272px;
    text-align: center; font-size: 15px; letter-spacing: .5px; line-height: 1.5;
  }
  .coverage strong { color: var(--brand-blue); font-weight: 700; }
  .band {
    position: absolute; left: 0; right: 0; bottom: 0; height: 62px;
    background: var(--brand-blue);
    display: flex; align-items: center; justify-content: center;
    font-weight: 700; font-size: 22px; letter-spacing: .4px; color: var(--text-light);
  }

  /* Back */
  .card--back { background: var(--paper); color: var(--text-dark); }
  .card--back .brand { left: 50px; top: 48px; }
  .company {
    position: absolute; right: 50px; top: 128px; text-align: right;
  }
  .company__name { color: var(--brand-blue); font-size: 30px; font-weight: 700; }
  .company__role { font-size: 17px; margin-top: 6px; letter-spacing: .4px; }
  .company__addr { font-size: 17px; line-height: 1.45; letter-spacing: .4px; margin-top: 4px; }

  .rule-contact {
    position: absolute; left: 50px; top: 230px; width: 330px; height: 1px; background: var(--ink);
  }
  .contacts {
    position: absolute; left: 50px; top: 244px; list-style: none;
    font-size: 18px; letter-spacing: .5px;
  }
  .contacts li { display: flex; align-items: center; gap: 12px; margin-bottom: 8px; }
  .contacts svg { width: 18px; height: 18px; flex: none; }
  .contacts .domain { color: var(--brand-blue); }

  .footer-band {
    position: absolute; left: 0; right: 0; bottom: 0; height: 54px;
    background: var(--ink);
    border-top: 3px solid var(--brand-blue);
    display: flex; align-items: center; justify-content: center;
    color: var(--text-light); font-size: 20px; letter-spacing: .8px;
  }
</style>
</head>
<body>
<main class="stage">

  <section class="card card--front" aria-label="Card front">
    <div class="brand">
      <span class="brand__dot"></span>
      <span class="brand__name">Bryncoed Locksmiths</span>
    </div>
    <ul class="services">
      <li>Emergency Lock Out</li>
      <li>uPVC</li>
      <li>Safe Specialists</li>
    </ul>
    <p class="values">PROMPT<span class="sep">|</span>LOCAL<span class="sep">|</span>RELIABLE</p>
    <p class="coverage"><strong>24h Emergency Service</strong><br>Covering All of North Wales, the Wirral and Chester</p>
    <div class="band">hello@bryncoedlocksmiths-demo.co.uk</div>
  </section>

  <section class="card card--back" aria-label="Card back">
    <div class="brand brand--on-paper">
      <span class="brand__dot"></span>
      <span class="brand__name">Bryncoed Locksmiths</span>
    </div>
    <div class="company">
      <p class="company__name">Bryncoed Locksmiths</p>
      <p class="company__role">Managing Director</p>
      <p class="company__addr">4 Pennant Rd., Hafod Barn<br>Llandudno LL39 7QZ</p>
    </div>
    <div class="rule-contact"></div>
    <ul class="contacts">
      <li>
        <svg viewBox="0 0 24 24" aria-hidden="true"><path fill="#26a9e0" d="M6.6 10.8a15.1 15.1 0 0 0 6.6 6.6l2.2-2.2c.3-.3.7-.4 1-.2 1.1.4 2.3.6 3.6.6.6 0 1 .4 1 1V20c0 .6-.4 1-1 1A17 17 0 0 1 3 4c0-.6.4-1 1-1h3.5c.6 0 1 .4 1 1 0 1.3.2 2.5.6 3.6.1.3 0 .7-.2 1z"/></svg>
        01632 960 725
      </li>
      <li>
        <svg viewBox="0 0 24 24" aria-hidden="true"><rect x="6" y="2" width="12" height="20" rx="2" fill="none" stroke="#26a9e0" stroke-width="2"/><circle cx="12" cy="18" r="1.2" fill="#26a9e0"/></svg>
        07700 900 362
      </li>
      <li>
        <svg viewBox="0 0 24 24" aria-hidden="true"><rect x="3" y="5" width="18" height="14" fill="none" stroke="#26a9e0" stroke-width="2"/><path d="M3 5l9 8 9-8" fill="none" stroke="#26a9e0" stroke-width="2"/></svg>
        <span>hello@<span class="domain">bryncoedlocksmiths-demo</span>.co.uk</span>
      </li>
    </ul>
    <div class="footer-band">Your Local Locksmith- No Job Too Small</div>
  </section>

</main>
</body>
</html>
```